Natural Light/Organic/Documentary Photography Business

I like a simple, approachable, feminine, earthy/organic feel. Earth/neutral tones, nothing too loud or obnoxious. I like the watercolor look. I don't want anything too trendy or something I'll get tired of after a couple months. As far as colors, I am much more a fan of cream/taupe/blue/green...not a fan of pink or purple at all.

Target Market(s)

Weddings & Families

Industry/Entity Type

Wedding Photography

Contact Information for Business Card

website, email, phone number

Font styles to use
Other font styles liked:
• Horizontes, Gotham

Colors

Designer to choose colors to be used in the design.

Requirements
Must have
• Website: www.meliskaverholt.com
• Phone: 482.319.6047
• Email: tessa@meliskaverholt.com
Nice to have
• I like the watercolor look but its not necessary. I like simple/earthy tones. Nothing too loud or distracting. Simple & feminine without being too girly. I like an approachable/soft feel.
• Instagram: www.instagram.com/meliskaverholtphotography/
Should not have
• NO loud colors or design or pattern. I do not want a photo of a camera or lens or anything cheesy like that.

```html
<!DOCTYPE html>
<html lang="en">
<head>
<meta charset="utf-8">
<title>Meliska Verholt Photography – Business Card</title>
<link href="https://fonts.googleapis.com/css2?family=Montserrat:wght@300;400&display=swap" rel="stylesheet">
<style>
  :root {
    --backdrop: #1f1f1f;
    --card-white: #fbfbfa;
    --taupe: #8a7e76;
    --taupe-soft: #a69d96;
    --photo-deep: #22301c;
    --photo-mid: #4a5e3a;
    --photo-light: #6f7f58;
    --ink-light: #ffffff;
  }
  * { margin: 0; padding: 0; box-sizing: border-box; }
  html, body {
    width: 1200px; height: 1200px; overflow: hidden;
    background: var(--backdrop);
    font-family: "Montserrat", sans-serif;
  }
  .canvas {
    position: relative; width: 1200px; height: 1200px;
    display: flex; flex-direction: column; align-items: center; justify-content: center; gap: 52px;
  }
  .card {
    position: relative; width: 900px; height: 514px;
    box-shadow: 0 18px 40px rgba(0,0,0,.55);
    overflow: hidden;
  }
  .card-front__photo {
    position: absolute; inset: 0;
    background:
      radial-gradient(ellipse at 52% 45%, var(--photo-light) 0%, var(--photo-mid) 40%, var(--photo-deep) 100%);
  }
  .card-front__shade { position: absolute; inset: 0; background: rgba(0,0,0,.22); }
  .card-back { background: var(--card-white); }
  .frame-corners { position: absolute; inset: 0; width: 100%; height: 100%; }
  .frame-corners--light path { stroke: var(--ink-light); }
  .frame-corners--taupe path { stroke: var(--taupe); }
  .frame-corners path { fill: none; stroke-width: 3; }
  .brand {
    position: absolute; left: 0; right: 0; text-align: center;
  }
  .brand__name {
    font-weight: 300; font-size: 54px; letter-spacing: 2px;
  }
  .brand__tag {
    font-weight: 300; font-size: 15px; letter-spacing: 9px; margin-top: 6px;
  }
  .card-front .brand { top: 210px; color: var(--ink-light); }
  .card-back .brand { top: 100px; color: var(--taupe); }
  .card-back .brand__name { font-size: 46px; }
  .card-back .brand__tag { font-size: 13px; color: var(--taupe-soft); }
  .contact {
    position: absolute; left: 0; right: 0; top: 262px;
    text-align: center; color: var(--taupe);
    font-weight: 300; font-size: 27px; line-height: 48px; letter-spacing: .5px;
  }
  .contact__sep { padding: 0 16px; }
</style>
</head>
<body>
<main class="canvas">
  <section class="card card-front">
    <div class="card-front__photo" role="img" aria-label="Portrait photograph of the photographer in a hat among green leafy plants"></div>
    <div class="card-front__shade"></div>
    <svg class="frame-corners frame-corners--light" viewBox="0 0 900 514" aria-hidden="true">
      <path d="M40 80 V40 H80"/>
      <path d="M820 40 H860 V80"/>
      <path d="M40 434 V474 H80"/>
      <path d="M820 474 H860 V434"/>
    </svg>
    <div class="brand">
      <div class="brand__name">Meliska Verholt</div>
      <div class="brand__tag">PHOTOGRAPHY</div>
    </div>
  </section>

  <section class="card card-back">
    <svg class="frame-corners frame-corners--taupe" viewBox="0 0 900 514" aria-hidden="true">
      <path d="M40 80 V40 H80"/>
      <path d="M820 40 H860 V80"/>
      <path d="M40 434 V474 H80"/>
      <path d="M820 474 H860 V434"/>
    </svg>
    <div class="brand">
      <div class="brand__name">Meliska Verholt</div>
      <div class="brand__tag">PHOTOGRAPHY</div>
    </div>
    <div class="contact">
      <div class="contact__phone">482.319.6047</div>
      <div>tessa@meliskaverholt.com<span class="contact__sep">|</span>www.meliskaverholt.com</div>
      <div class="contact__address">Your address, city, state, ZIP 0000</div>
    </div>
  </section>
</main>
</body>
</html>
```